Organic Sunscreen Business "VelloraPure" Needs Package Design

Our company VelloraPure, manufactures an anti-ageing SPF 15 sunscreen product.

We specialise in the world's most rare and luxury organic anti-ageing ingredients.

We require an attractive package design for a 2.5 oz/75 ml squeezy bottle with box design, a few examples of similar examples which we like are attached.

We have a logo, barcode and graphic, which has been uploaded, and the bottle is to convey the message of wealth and luxury as well as organic sunscreen, we would prefer the package to be colourful and creative in order to sell.

I have included 2 rough sketches of the basic elements and layout of the design. And the box is to be similar to the bottle but to contain an extra caption.

Also, the sketch is only for a guide on how I would like the package, i.e. the labels and graphics can be in different positions/layouts thanks. And any additional creative images, text or fonts would be considered.

Industry/Entity Type

Business

Requirements
Must have
• FRONT of Bottle:
• LABEL 1: Logo (attached)
• LABEL 2:
• SPF 15
• Non-Nano
• Technology
• 100% Organic
• Paraben Free
• LABEL 3: (Larger/higher emphasis than Label 2)
• Anti-Ageing
• Moisturiser
• BACK of Bottle:
• Introduction: (For me to add personally at later date)
• Warnings: For external use only. Do not use on damaged or broken skin. Stop use and ask a doctor if rash occurs. When using this product keep out of eyes. Rinse with water to remove.
• Directions: Shake well before use. Apply liberally 15 minutes before sun exposure. Use a water resistant sunscreen if swimming or sweating. Reapply at least every 2 hours. Children under 6 months: Ask a doctor.
• Active Ingredient: Non-Nano Zinc Oxide (6%)
• Also contains: (For me to add personally at later date)
• Barcode: (image attached)
• Contact: www.vellorapure-example.com.au
• 2.5oz/7ml e
• BOX:
• Same as bottle, but one side will contain the caption:
• "7 NATURAL WONDERS IN 1" (In a creative style)
Nice to have
• Additional Text/Images/Fonts relating to the subject(s)
• Most creative design will be the winner.

```html
<!DOCTYPE html>
<html lang="en">
<head>
<meta charset="utf-8">
<title>VelloraPure – SPF 15 Anti-Ageing Moisturiser Packaging</title>
<link rel="stylesheet" href="https://fonts.googleapis.com/css2?family=Cinzel:wght@400;700&display=swap">
<style>
  :root {
    --backdrop-top: #c9a2a4;
    --backdrop-bottom: #a98386;
    --panel-base: #eef5fa;
    --pattern-tone: #d6e8f4;
    --ink-blue: #2f7cc0;
    --brand-gold: #c29a45;
    --sun-orange: #f6a524;
    --sun-light: #fbd27a;
    --river-blue: #3f86c4;
    --shore-green: #4f8a43;
    --pyramid-sand: #e8b25a;
    --cap-orange: #f08a10;
    --cap-shine: #ffc05a;
    --caption-white: #ffffff;
  }
  * { box-sizing: border-box; margin: 0; padding: 0; }
  html, body { width: 1200px; height: 780px; overflow: hidden; }
  body {
    background: radial-gradient(ellipse at 50% 40%, var(--backdrop-top), var(--backdrop-bottom));
    font-family: "Cinzel", Georgia, serif;
    color: var(--ink-blue);
    position: relative;
  }
  .panel {
    position: absolute;
    top: 110px;
    height: 560px;
    background: var(--panel-base);
    overflow: hidden;
  }
  .panel-pattern {
    position: absolute; inset: 0;
    background: linear-gradient(180deg, var(--panel-base), var(--pattern-tone));
  }
  .panel-scene {
    position: absolute; left: 0; right: 0; bottom: 0; height: 150px;
    background: linear-gradient(180deg, var(--pyramid-sand) 0%, var(--pyramid-sand) 30%, var(--shore-green) 42%, var(--river-blue) 55%, var(--panel-base) 100%);
  }
  .box-side { left: 250px; width: 160px; }
  .box-front { left: 410px; width: 220px; box-shadow: inset 1px 0 0 rgba(0,0,0,0.08); }
  .tube { left: 720px; width: 250px; height: 470px; border-radius: 6px 6px 0 0; }
  .tube-cap {
    position: absolute; left: 728px; top: 580px; width: 234px; height: 90px;
    border-radius: 4px 4px 10px 10px;
    background: linear-gradient(90deg, var(--cap-orange), var(--cap-shine) 45%, var(--cap-orange));
  }
  .tube .panel-scene { height: 110px; bottom: 0; }

  .caption-sun {
    position: absolute; left: 10px; top: 150px; width: 140px; height: 140px;
    border-radius: 50%;
    background: radial-gradient(circle, var(--sun-orange) 60%, var(--sun-light));
    display: flex; align-items: center; justify-content: center;
  }
  .caption-text {
    position: absolute; left: 10px; top: 150px; width: 140px; height: 140px;
    display: flex; flex-direction: column; align-items: center; justify-content: center;
    color: var(--caption-white); font-weight: 700; font-size: 17px; line-height: 1.1; text-align: center;
  }
  .caption-text .numeral { font-size: 20px; }

  .label-stack {
    position: absolute; left: 0; right: 0; top: 38px;
    display: flex; flex-direction: column; align-items: center; text-align: center;
  }
  .brand-mark { display: flex; align-items: center; gap: 6px; margin-bottom: 22px; }
  .brand-dot { width: 10px; height: 10px; border-radius: 50%; background: var(--brand-gold); }
  .brand-name { color: var(--brand-gold); font-size: 17px; font-weight: 400; }
  .claims { list-style: none; font-weight: 700; font-size: 15px; line-height: 1.15; }
  .claims li { margin-bottom: 9px; }
  .highlight { margin-top: 12px; font-weight: 700; font-size: 11px; display: flex; flex-direction: column; align-items: center; gap: 4px; }
  .highlight-sun {
    width: 22px; height: 22px; border-radius: 50%;
    background: radial-gradient(circle, var(--sun-orange) 30%, var(--sun-light) 60%, transparent 72%);
  }
  .tube .label-stack { top: 52px; }
  .tube .brand-name { font-size: 19px; }
  .tube .claims { font-size: 16px; }
  .tube .highlight { font-size: 12px; }
</style>
</head>
<body>
  <section class="panel box-side" aria-label="Box side panel">
    <div class="panel-pattern" role="img" aria-label="Soft blue damask pattern background"></div>
    <div class="panel-scene" role="img" aria-label="Sketched pyramids above a green shoreline and blue river"></div>
    <div class="caption-sun" role="img" aria-label="Orange sunburst"></div>
    <p class="caption-text"><span class="numeral">7</span><span>Natural</span><span>Wonders</span><span>in 1</span></p>
  </section>

  <section class="panel box-front" aria-label="Box front panel">
    <div class="panel-pattern" role="img" aria-label="Soft blue damask pattern background"></div>
    <div class="panel-scene" role="img" aria-label="Sketched pyramids above a green shoreline and blue river"></div>
    <div class="label-stack">
      <div class="brand-mark"><span class="brand-dot"></span><span class="brand-name">VelloraPure</span></div>
      <ul class="claims">
        <li>SPF 15</li>
        <li>Non-Nano<br>Technology</li>
        <li>100% Organic</li>
        <li>Paraben Free</li>
      </ul>
      <div class="highlight"><span>Anti-Ageing</span><span class="highlight-sun"></span><span>Moisturiser</span></div>
    </div>
  </section>

  <section class="panel tube" aria-label="Tube label">
    <div class="panel-pattern" role="img" aria-label="Soft blue damask pattern background"></div>
    <div class="panel-scene" role="img" aria-label="Sketched pyramids above a green shoreline and blue river"></div>
    <div class="label-stack">
      <div class="brand-mark"><span class="brand-dot"></span><span class="brand-name">VelloraPure</span></div>
      <ul class="claims">
        <li>SPF 15</li>
        <li>Non-Nano<br>Technology</li>
        <li>100% Organic</li>
        <li>Paraben Free</li>
      </ul>
      <div class="highlight"><span>Anti-Ageing</span><span class="highlight-sun"></span><span>Moisturiser</span></div>
    </div>
  </section>
  <div class="tube-cap" aria-hidden="true"></div>
</body>
</html>
```